Brindle's Botanic's. I make and sell organic bath & body products. Nourishing bath & body products. Products are soaps, scrubs, lip balms, bath salts, baby & mother products (belly balm, nipple balm, diaper balm, baby bath soak, chest rub,) . I use botanical and or herbs in all my recipes. I create my own recipes. I like muted colors...but I would like something that will get your attention. I like the colors green and brown, but open to any other colors. I would also like to get information about labels (different sizes for my products) I do like the pasley print and maybe even a cute owl.

Target Market(s)

women, pregnant and nursing women, women with children and men

Industry/Entity Type

Baby

Contact Information for Business Card

Mona Greeley
517-384-2706,mgreeley@tallowmail.example
mgreeley@tallowmail.example

Font styles to use
Other font styles liked:
• bree

Requirements
Must have
• Brindle's Botanic's, nourishing bath & body products. It needs to get a person attention. I would like to see cards that are hip and fun. I would also like to view cards that are classy. I do like muted colors but I do have an open mind (use any color you think would be right) So far a lot of the cards have had leaves....I really do not like that design.
Nice to have
• ???pasley in the background ?cute owl
Should not have
• leaves

```html
<!DOCTYPE html>
<html lang="en">
<head>
<meta charset="utf-8">
<title>Brindle's Botanic's – Business Card</title>
<link href="https://fonts.googleapis.com/css2?family=Dancing+Script:wght@700&family=Cambo&family=Arimo&display=swap" rel="stylesheet">
<style>
  :root {
    --bark: #4a1d16;
    --bark-stripe: rgba(255, 235, 225, 0.06);
    --bark-glow: rgba(150, 90, 75, 0.35);
    --cream: #ffffff;
    --sprout: #45aa4a;
  }
  html, body {
    margin: 0;
    padding: 0;
    width: 1200px;
    height: 704px;
    overflow: hidden;
    background: var(--bark);
  }
  .card {
    position: relative;
    width: 1200px;
    height: 704px;
    overflow: hidden;
    background:
      radial-gradient(ellipse 55% 60% at 50% 48%, var(--bark-glow), transparent 75%),
      repeating-linear-gradient(165deg, transparent 0 30px, var(--bark-stripe) 30px 60px),
      var(--bark);
  }
  .owner-name {
    position: absolute;
    left: 68px;
    top: 26px;
    margin: 0;
    font-family: "Dancing Script", cursive;
    font-weight: 700;
    font-size: 46px;
    color: var(--cream);
  }
  .brand {
    position: absolute;
    left: 164px;
    top: 244px;
    display: flex;
    align-items: center;
    gap: 28px;
  }
  .brand-dot {
    width: 110px;
    height: 110px;
    border-radius: 50%;
    background: var(--sprout);
  }
  .brand-name {
    margin: 0;
    font-family: "Cambo", serif;
    font-weight: 400;
    font-size: 82px;
    line-height: 1;
    color: var(--cream);
    text-shadow: 0 2px 4px rgba(0, 0, 0, 0.35);
  }
  .contact-panel {
    position: absolute;
    left: 205px;
    top: 565px;
    width: 790px;
    height: 139px;
    background: var(--sprout);
    display: flex;
    flex-direction: column;
    justify-content: center;
    align-items: center;
    gap: 6px;
    font-family: "Arimo", Arial, sans-serif;
    font-size: 31px;
    color: var(--cream);
  }
  .contact-line { margin: 0; }
</style>
</head>
<body>
  <main class="card">
    <p class="owner-name">Mona Greeley</p>
    <div class="brand">
      <div class="brand-dot"></div>
      <h1 class="brand-name">Brindle's Botanic's</h1>
    </div>
    <section class="contact-panel">
      <p class="contact-line">Ph.: 517-384-2706</p>
      <p class="contact-line">E-mail: mgreeley@tallowmail.example</p>
    </section>
  </main>
</body>
</html>
```